Stationery Design Project

KT7 Staffing requires letterhead and business card designs for a company based in London. Just like the name, we're a management resourcing company, providing resources to third party companies. You can see www.kt7staffing-example.com for ideas on existing colour schemes and design concepts that have been implimented and agreed to. Ultimately the design should broadcast professionalism, safety and the concept of growth.

Target Market(s)

Financial institutes; friendly societies (All UK based)

Industry/Entity Type

Safety

Requirements
Must have
• Files produced should be print ready; and the text in them editable (eg address, name etc)

```html
<!DOCTYPE html>
<html lang="en">
<head>
<meta charset="utf-8">
<title>KT7 Staffing – Business Card</title>
<link href="https://fonts.googleapis.com/css2?family=Arimo:wght@700&family=Open+Sans:wght@400;600&display=swap" rel="stylesheet">
<style>
  :root {
    --backdrop: #f2557c;
    --card: #3a3d41;
    --card-edge: #2b2d30;
    --brand-teal: #2ba3a9;
    --brand-sky: #6fc3df;
    --text-light: #ffffff;
  }
  * { margin: 0; padding: 0; box-sizing: border-box; }
  html, body {
    width: 1200px;
    height: 900px;
    overflow: hidden;
    background: var(--backdrop);
  }
  .business-card {
    position: absolute;
    left: 2px;
    top: 110px;
    width: 1194px;
    height: 680px;
    background: var(--card);
    border: 2px solid var(--card-edge);
    border-radius: 24px;
    color: var(--text-light);
  }
  .brand {
    position: absolute;
    left: 56px;
    top: 170px;
    display: flex;
    align-items: center;
    gap: 22px;
  }
  .brand-mark {
    width: 60px;
    height: 60px;
    background: var(--brand-sky);
  }
  .brand-name {
    font-family: "Open Sans", sans-serif;
    font-weight: 600;
    font-size: 84px;
    line-height: 1;
    color: var(--brand-teal);
    letter-spacing: 1px;
  }
  .website {
    position: absolute;
    left: 192px;
    top: 294px;
    font-family: "Open Sans", sans-serif;
    font-weight: 400;
    font-size: 34px;
    letter-spacing: 2px;
  }
  .contact-person {
    position: absolute;
    left: 58px;
    top: 474px;
  }
  .person-name {
    font-family: "Arimo", sans-serif;
    font-weight: 700;
    font-size: 41px;
    line-height: 1.2;
  }
  .person-role {
    font-family: "Arimo", sans-serif;
    font-weight: 700;
    font-size: 31px;
    margin-top: 4px;
  }
  .person-email {
    font-family: "Open Sans", sans-serif;
    font-size: 34px;
    margin-top: 10px;
  }
  .company-details {
    position: absolute;
    right: 52px;
    top: 478px;
    text-align: right;
    font-family: "Open Sans", sans-serif;
    font-size: 35px;
    letter-spacing: 1px;
    line-height: 1.1;
  }
  .company-details .address { margin-bottom: 22px; }
  .company-details .phone { margin-bottom: 12px; }
</style>
</head>
<body>
  <div class="business-card">
    <div class="brand">
      <div class="brand-mark"></div>
      <div class="brand-name">KT7 Staffing</div>
    </div>
    <div class="website">www.kt7staffing-example.com</div>

    <div class="contact-person">
      <div class="person-name">Daniel Hart</div>
      <div class="person-role">Director</div>
      <div class="person-email">danielh@kt7staffing-example.com</div>
    </div>

    <div class="company-details">
      <div class="address">18, Elm Row, London</div>
      <div class="phone">M. 1-555-014-362</div>
      <div class="phone">T. 0207 946-0183</div>
    </div>
  </div>
</body>
</html>
```